a graphic model of stress response for online learning course

We need a model of how the brain experiences, interprets and responds to stressors. There are three components to this.

I need a simple linear graphic of the three stages with arrows between to show progression:
1. We experience the stressor
2. Our brain interprets the stressor: Is it a threat? Is it friendly?
3. Our brain creates the appropriate stress response: physical, mental, emotional

And another graphic with illustrations of this process:
A charging lion
A brain thinking/interpreting the potential stressor
A person running away (the response to the threat).

Needs to be used for online learning course about stress and resilience.

See attached for assistance.

```html
<!DOCTYPE html>
<html lang="en">
<head>
<meta charset="utf-8">
<title>Stress Response Model</title>
<link rel="stylesheet" href="https://fonts.googleapis.com/css2?family=Montserrat:wght@600;700&display=swap">
<style>
  :root {
    --paper: #ffffff;
    --night: #1b1b1b;
    --ink: #2b2b2b;
    --silhouette: #2e2e2e;
    --orange-light: #fb9558;
    --orange-deep: #f5711c;
    --orange-badge: #f6782a;
    --grey-light: #c2c2c2;
    --grey-deep: #9e9e9e;
    --grey-badge: #a8a8a8;
    --yellow-light: #fdd640;
    --yellow-deep: #f4c200;
    --yellow-badge: #fbcd12;
    --edge: #ffffff;
  }
  html, body {
    margin: 0;
    padding: 0;
    width: 1200px;
    height: 1000px;
    overflow: hidden;
    background: var(--paper);
  }
  .canvas {
    display: block;
    width: 1200px;
    height: 1000px;
  }
  .band-light { fill: var(--paper); }
  .band-dark { fill: var(--night); }
  .step-number {
    font-family: "Montserrat", sans-serif;
    font-weight: 700;
    font-size: 24px;
    fill: var(--ink);
    text-anchor: middle;
  }
  .step-caption {
    font-family: "Montserrat", sans-serif;
    font-weight: 700;
    font-size: 13px;
    fill: var(--ink);
  }
  .chevron, .caption-tab { stroke: var(--edge); stroke-width: 1.5; }
  .badge { stroke: var(--edge); stroke-width: 2; }
  .illustration { fill: var(--silhouette); }
</style>
</head>
<body>
<svg class="canvas" viewBox="0 0 1200 1000" xmlns="http://www.w3.org/2000/svg">
  <defs>
    <linearGradient id="orange-fill" x1="0" y1="0" x2="1" y2="1">
      <stop offset="0" stop-color="var(--orange-light)"/>
      <stop offset="1" stop-color="var(--orange-deep)"/>
    </linearGradient>
    <linearGradient id="grey-fill" x1="0" y1="0" x2="1" y2="1">
      <stop offset="0" stop-color="var(--grey-light)"/>
      <stop offset="1" stop-color="var(--grey-deep)"/>
    </linearGradient>
    <linearGradient id="yellow-fill" x1="0" y1="0" x2="1" y2="1">
      <stop offset="0" stop-color="var(--yellow-light)"/>
      <stop offset="1" stop-color="var(--yellow-deep)"/>
    </linearGradient>
    <filter id="soft-shadow" x="-20%" y="-20%" width="140%" height="140%">
      <feDropShadow dx="3" dy="4" stdDeviation="5" flood-color="#000" flood-opacity="0.22"/>
    </filter>

    <g id="stress-flow">
      <!-- Step 1 -->
      <g class="step step-experience">
        <path class="chevron" filter="url(#soft-shadow)" fill="url(#orange-fill)"
              d="M223,127 H445 L502,224 L445,321 H223 L278,224 Z"/>
        <path class="caption-tab" filter="url(#soft-shadow)" fill="url(#orange-fill)"
              d="M220,288 H413 A41.5,41.5 0 0 1 413,371 H220 Z"/>
        <rect class="illustration" role="img" aria-label="Silhouette of a charging lion"
              x="276" y="180" width="161" height="114" rx="30"/>
        <circle class="badge" cx="294" cy="133" r="26" fill="var(--orange-badge)"/>
        <text class="step-number" x="294" y="142">01</text>
        <text class="step-caption" x="237" y="322">We experience</text>
        <text class="step-caption" x="237" y="337">the stressor</text>
      </g>
      <!-- Step 2 -->
      <g class="step step-interpret">
        <path class="chevron" filter="url(#soft-shadow)" fill="url(#grey-fill)"
              d="M479,127 H701 L758,224 L701,321 H479 L534,224 Z"/>
        <path class="caption-tab" filter="url(#soft-shadow)" fill="url(#grey-fill)"
              d="M477,288 H670 A41.5,41.5 0 0 1 670,371 H477 Z"/>
        <rect class="illustration" role="img" aria-label="Silhouette of a head in profile with a questioning brain"
              x="555" y="167" width="110" height="121" rx="40"/>
        <circle class="badge" cx="550" cy="133" r="26" fill="var(--grey-badge)"/>
        <text class="step-number" x="550" y="142">02</text>
        <text class="step-caption" x="492" y="321">Our brain interprets</text>
        <text class="step-caption" x="492" y="336">the stressor:</text>
        <text class="step-caption" x="492" y="351">Is it a threat? Is it friendly?</text>
      </g>
      <!-- Step 3 -->
      <g class="step step-respond">
        <path class="chevron" filter="url(#soft-shadow)" fill="url(#yellow-fill)"
              d="M734,127 H956 L1013,224 L956,321 H734 L789,224 Z"/>
        <path class="caption-tab" filter="url(#soft-shadow)" fill="url(#yellow-fill)"
              d="M733,288 H926 A41.5,41.5 0 0 1 926,371 H733 Z"/>
        <rect class="illustration" role="img" aria-label="Silhouette of a person running away"
              x="810" y="151" width="114" height="147" rx="30"/>
        <circle class="badge" cx="808" cy="133" r="26" fill="var(--yellow-badge)"/>
        <text class="step-number" x="808" y="142">03</text>
        <text class="step-caption" x="748" y="321">Our brain creates the</text>
        <text class="step-caption" x="748" y="336">appropriate stress response:</text>
        <text class="step-caption" x="748" y="351">physical, mental, emotional</text>
      </g>
    </g>
  </defs>

  <rect class="band-light" x="0" y="0" width="1200" height="484"/>
  <rect class="band-dark" x="0" y="484" width="1200" height="516"/>

  <use href="#stress-flow"/>
  <use href="#stress-flow" y="473"/>
</svg>
</body>
</html>
```